Wedding filmmaker needs artistic business card design - brightwaterreels.ca

We are high end wedding filmmakers in a major market who produce cinematic wedding films. We require a business card design that communicates our quality, artistry, and professionalism yet looks progressive and friendly. Colors and design should skew appeal more to the bride-to-be who is usually the decision maker but not be overtly feminine per se. This means generally light pastel shades of ivory, purple, pink, yellow, as examples.
We already have a name logo established: the words "Brightwater Reels" in the font Great Vibes. Designs must use Tallow natural cardstock as the print stock and am leaning heavily toward our name logo in white, but I am open to black as well. Please design any color elements with spot white underneath where possible.
Do not try to compliment or take inspiration from our website design. Treat the card design as a separate stand alone.
Thank you so much for your hard work!

Target Market(s)

Affluent couples spending $50,000+ on their wedding

Industry/Entity Type

Progressive

Contact Information for Business Card

Paul Brightwater
Producer
905-418-2937
www.brightwaterreels.ca
paul@brightwaterreels.ca
twitter @brightwater762

Font styles to use
Serif
Sans Serif

Requirements
Must have
• - Brightwater Reels name logo (reference GIF uploaded for reference only) and catch phrase: Breathtaking wedding films (I'm open to capitalizing all three words, or just first, or all in small caps). I favor logo, and catch phrase on front of card and my contact details on the other side but if you feel strongly about a different design, go for it!
• - Design must be submitted shown on Tallow natural cardstock NOT WHITE cardstock, If you're not familiar with Tallow, this is what it looks like: http://www.quillandtwinejournal.com/wp-content/uploads/2013/07/il_570xN.837264019_kq4m.jpg
Nice to have
• - An original graphic element (eg. movie reel, bouquet, confetti, etc.) that compliments the name logo but is subtle and discreet, doesn't overpower or entangle it.
• -Great use of balance, composition, negative space, etc. I like clean tasteful design
Should not have
• -Lousy boring clip art.
• -Graphic elements, fonts, or color palette from our website
• -White cardstock background
• -designs you have previously submitted for other contests
• -Bold dark colors (eg. red, orange navy blue, etc.)
• -High tech futuristic designs like you'd create for a software company

```html
<!DOCTYPE html>
<html lang="en">
<head>
<meta charset="utf-8">
<title>Brightwater Reels — Business Card</title>
<link href="https://fonts.googleapis.com/css2?family=Great+Vibes&family=Questrial&family=Cormorant+Garamond:wght@500&display=swap" rel="stylesheet">
<style>
  :root {
    --backdrop: #e9e6e1;
    --stock: #efe3cb;
    --stock-shade: #e6d7ba;
    --lilac: #b7a2c6;
    --blush: #f1d3d6;
    --ink: #6a5676;
    --ink-soft: #7d6d80;
    --rule: #b9a8b8;
  }
  * { margin: 0; padding: 0; box-sizing: border-box; }
  html, body { width: 1200px; height: 900px; overflow: hidden; }
  body {
    background: var(--backdrop);
    display: flex;
    flex-direction: column;
    align-items: center;
    justify-content: center;
    gap: 40px;
    font-family: "Questrial", sans-serif;
    color: var(--ink-soft);
  }
  .card {
    position: relative;
    width: 700px;
    height: 400px;
    border-radius: 38px;
    overflow: hidden;
    background: linear-gradient(160deg, var(--stock) 45%, var(--stock-shade) 100%);
    box-shadow: 0 6px 18px rgba(0,0,0,0.12);
  }
  .card .swoosh { position: absolute; inset: 0; width: 100%; height: 100%; }
  .wordmark {
    position: absolute;
    font-family: "Great Vibes", cursive;
    font-weight: 400;
    color: var(--ink);
    white-space: nowrap;
  }
  .tagline {
    position: absolute;
    font-family: "Cormorant Garamond", serif;
    font-weight: 500;
    font-variant: small-caps;
    letter-spacing: 4px;
    color: var(--ink-soft);
    white-space: nowrap;
  }
  .card-front .wordmark { top: 30px; left: 0; right: 0; text-align: center; font-size: 76px; }
  .card-front .tagline { top: 128px; left: 0; right: 0; text-align: center; font-size: 21px; }
  .card-back .wordmark { top: 110px; left: 250px; font-size: 64px; }
  .card-back .tagline { top: 200px; left: 300px; font-size: 21px; }

  .details {
    position: absolute;
    top: 192px;
    left: 130px;
    display: flex;
    font-variant: small-caps;
    letter-spacing: 2px;
    font-size: 19px;
    line-height: 1.25;
  }
  .identity { text-align: right; padding-right: 16px; }
  .identity .name { font-weight: 700; color: var(--ink); letter-spacing: 2.5px; }
  .divider { width: 1px; height: 104px; background: var(--rule); }
  .contacts { list-style: none; padding-left: 16px; }
  .contacts li { display: flex; align-items: center; gap: 8px; }
  .contacts svg { width: 14px; height: 14px; flex: none; }
</style>
</head>
<body>

  <section class="card card-front">
    <svg class="swoosh" viewBox="0 0 700 400" preserveAspectRatio="none" aria-hidden="true">
      <path d="M0,275 C150,345 390,375 700,392 L700,400 L0,400 Z" fill="var(--lilac)"/>
      <path d="M0,302 C160,360 380,385 600,398" fill="none" stroke="var(--blush)" stroke-width="5"/>
    </svg>
    <h1 class="wordmark">Brightwater Reels</h1>
    <p class="tagline">Breathtaking Wedding Films</p>
    <div class="details">
      <div class="identity">
        <div class="name">Paul Brightwater</div>
        <div class="role">Producer</div>
      </div>
      <div class="divider"></div>
      <ul class="contacts">
        <li><svg viewBox="0 0 14 14"><circle cx="7" cy="7" r="7" fill="var(--lilac)"/><path d="M4.5 3.5l1.5 0 .6 2-1 .8a5 5 0 0 0 2.1 2.1l.8-1 2 .6 0 1.5c-3.6.3-6.3-2.4-6-6z" fill="#fff"/></svg>905-418-2937</li>
        <li><svg viewBox="0 0 14 14"><circle cx="7" cy="7" r="7" fill="var(--lilac)"/><rect x="3.5" y="4.5" width="7" height="5" fill="#fff"/><path d="M3.5 4.5l3.5 3 3.5-3" fill="none" stroke="var(--lilac)" stroke-width="0.8"/></svg>paul@brightwaterreels.ca</li>
        <li><svg viewBox="0 0 14 14"><circle cx="7" cy="7" r="7" fill="var(--lilac)"/><circle cx="7" cy="7" r="3.6" fill="none" stroke="#fff" stroke-width="1"/><path d="M3.4 7h7.2M7 3.4v7.2" stroke="#fff" stroke-width="0.8"/></svg>www.brightwaterreels.ca</li>
        <li><svg viewBox="0 0 14 14"><circle cx="7" cy="7" r="7" fill="var(--lilac)"/><circle cx="7" cy="7" r="2.4" fill="#fff"/></svg>twitter @brightwater762</li>
      </ul>
    </div>
  </section>

  <section class="card card-back">
    <svg class="swoosh" viewBox="0 0 700 400" preserveAspectRatio="none" aria-hidden="true">
      <path d="M0,10 C110,220 360,350 700,372 L700,400 L560,400 C300,370 90,260 0,120 Z" fill="var(--lilac)"/>
      <path d="M0,-10 C120,200 370,330 700,352" fill="none" stroke="var(--blush)" stroke-width="4"/>
    </svg>
    <h2 class="wordmark">Brightwater Reels</h2>
    <p class="tagline">Breathtaking Wedding Films</p>
  </section>

</body>
</html>
```